Kestrel Roofing & Restoration Business Card Design

Lookiing for a double sided business card design that will have rounded corners, will look good with Spot UV, Soft Laminate, or Gloss
Front of card should have Logo, Name and Contact Info, License numbers
Back of card should have Logo, maybe other small details

```html
<!DOCTYPE html>
<html lang="en">
<head>
<meta charset="utf-8">
<title>Kestrel Roofing &amp; Restoration – Business Cards</title>
<link rel="stylesheet" href="https://fonts.googleapis.com/css2?family=Montserrat:wght@500;600;700;800&family=Arimo:wght@400&display=swap">
<style>
  :root {
    --bg: #2b2b2b;
    --card-dark: #0e0d0e;
    --card-mid: #2a2a2b;
    --white: #ffffff;
    --blue: #1fa3e0;
    --soft: #e6e6e6;
  }
  * { box-sizing: border-box; margin: 0; padding: 0; }
  html, body { width: 1200px; height: 800px; overflow: hidden; }
  body {
    background: var(--bg);
    font-family: "Montserrat", sans-serif;
    position: relative;
  }
  .card {
    position: absolute;
    width: 540px;
    height: 310px;
    border-radius: 20px;
    overflow: hidden;
    background: linear-gradient(160deg, var(--card-dark) 0%, var(--card-mid) 48%, var(--card-dark) 100%);
    box-shadow: 0 10px 30px rgba(0,0,0,.45);
  }
  .card--back { left: 40px; top: 245px; }
  .card--front { left: 620px; top: 245px; }

  .brand {
    display: flex;
    align-items: center;
    gap: 10px;
    color: var(--white);
    font-weight: 600;
    text-transform: uppercase;
    letter-spacing: .02em;
    line-height: 1.1;
  }
  .brand__square {
    width: 14px; height: 14px;
    background: var(--blue);
    flex: none;
  }
  .card--back .brand {
    position: absolute;
    left: 50%; top: 50%;
    transform: translate(-50%, -50%);
    font-size: 22px;
    white-space: nowrap;
  }
  .card--front .brand {
    position: absolute;
    left: 270px; top: 34px;
    font-size: 15px;
  }

  .person { position: absolute; left: 32px; top: 132px; }
  .person__name {
    color: var(--blue);
    font-weight: 800;
    font-size: 20px;
    letter-spacing: .01em;
    text-transform: uppercase;
  }
  .person__role {
    color: var(--soft);
    font-family: "Arimo", sans-serif;
    font-size: 14px;
    margin-top: 2px;
  }

  .contact {
    position: absolute;
    left: 330px; top: 118px;
    padding-left: 18px;
    border-left: 1.5px solid var(--blue);
    list-style: none;
    font-family: "Arimo", sans-serif;
    font-size: 13px;
    color: var(--soft);
  }
  .contact__item {
    display: flex;
    align-items: flex-start;
    gap: 10px;
    line-height: 1.35;
    margin-bottom: 3px;
  }
  .contact__icon { width: 12px; height: 12px; flex: none; margin-top: 2px; }

  .wordmark-large {
    position: absolute;
    left: 40px; bottom: -44px;
    color: var(--white);
    font-weight: 800;
    font-size: 132px;
    letter-spacing: -.02em;
    line-height: 1;
    text-transform: uppercase;
  }
</style>
</head>
<body>

  <section class="card card--back" aria-label="Card back">
    <div class="brand">
      <span class="brand__square"></span>
      <span>Kestrel Roofing<br>&amp; Restoration</span>
    </div>
  </section>

  <section class="card card--front" aria-label="Card front">
    <div class="brand">
      <span class="brand__square"></span>
      <span>Kestrel Roofing<br>&amp; Restoration</span>
    </div>

    <div class="person">
      <p class="person__name">Daniel Harper</p>
      <p class="person__role">Founder &amp; Director</p>
    </div>

    <ul class="contact">
      <li class="contact__item">
        <svg class="contact__icon" viewBox="0 0 12 12" aria-hidden="true"><rect x="2.5" y="0.5" width="7" height="11" rx="1.5" fill="none" stroke="var(--blue)" stroke-width="1.3"/><rect x="5" y="9" width="2" height="1" fill="var(--blue)"/></svg>
        <span>044-987 654 321</span>
      </li>
      <li class="contact__item">
        <svg class="contact__icon" viewBox="0 0 12 12" aria-hidden="true"><path d="M0.5 5.5 L11.5 0.5 L7 11.5 L5.5 7 Z" fill="var(--blue)"/></svg>
        <span>info@kestrelroof.com</span>
      </li>
      <li class="contact__item">
        <svg class="contact__icon" viewBox="0 0 12 12" aria-hidden="true"><circle cx="6" cy="6" r="5.3" fill="none" stroke="var(--blue)" stroke-width="1.2"/><ellipse cx="6" cy="6" rx="2.3" ry="5.3" fill="none" stroke="var(--blue)" stroke-width="1"/><line x1="0.7" y1="6" x2="11.3" y2="6" stroke="var(--blue)" stroke-width="1"/></svg>
        <span>www.kestrelroof.com</span>
      </li>
      <li class="contact__item">
        <svg class="contact__icon" viewBox="0 0 12 12" aria-hidden="true"><path d="M6 11.5 C3 8 2 6.5 2 4.5 A4 4 0 0 1 10 4.5 C10 6.5 9 8 6 11.5 Z" fill="var(--blue)"/><circle cx="6" cy="4.5" r="1.5" fill="var(--card-dark)"/></svg>
        <span>4510 Harbor Bay Pkwy<br>212-B, FL 32541</span>
      </li>
    </ul>

    <div class="wordmark-large">Kestrel</div>
  </section>

</body>
</html>
```